Business Card Design

Tumble Nook is a Laundromat Store
we provide wash and Fold service to Customers who are busy with their life and can not come to the store and do laundry
we have customers who drop their laundry at the store
but now i want to provide service to customers who are not able to come to the store to drop. i will go to their address and pickup the laundry and get it washed folded and delivered
Updates
Can you use the colour in you design which i uploaded and also fusha fluorescent green bright pink
Target Market(s)
all works of life who don't have time to do laundry
Industry/Entity Type
Store
Contact Information for Business Card
TumbleNook Laundromat
284 Colbrook Street
Lynn MA 01957
Look and feel
Each slider illustrates characteristics of the customer's brand and the style your logo design should communicate.

```html
<!DOCTYPE html>
<html lang="en">
<head>
<meta charset="utf-8">
<title>Tumble Nook Laundromat – Business Card</title>
<link rel="stylesheet" href="https://fonts.googleapis.com/css2?family=Quicksand:wght@500&family=Open+Sans:wght@700&display=swap">
<style>
  :root {
    --page-bg: #ebe6dc;
    --leaf: #2f9a3e;
    --forest: #1e8c3a;
    --lime: #b9d83a;
    --lime-soft: #dfe98a;
    --cream: #f7f6dc;
    --ring: #7ccf5a;
    --ring-deep: #3fae4a;
    --fuchsia: #e0387a;
    --pink: #f28bb0;
    --white: #ffffff;
  }
  html, body {
    margin: 0;
    width: 1200px;
    height: 1023px;
    overflow: hidden;
    background: var(--page-bg);
  }
  .business-card {
    position: absolute;
    left: 110px;
    top: 231px;
    width: 980px;
    height: 560px;
    overflow: hidden;
    border-radius: 6px;
    background: linear-gradient(100deg, var(--lime) 0%, var(--lime-soft) 22%, var(--cream) 48%, var(--cream) 70%, var(--lime-soft) 100%);
    box-shadow: 0 6px 24px rgba(0,0,0,0.18);
  }
  .brand {
    position: absolute;
    left: 56px;
    top: 232px;
    display: flex;
    align-items: center;
    gap: 18px;
  }
  .brand-dot {
    width: 56px;
    height: 56px;
    border-radius: 50%;
    background: var(--ring-deep);
    flex: none;
  }
  .brand-text { display: flex; flex-direction: column; }
  .brand-name {
    font-family: "Quicksand", sans-serif;
    font-weight: 500;
    font-size: 66px;
    line-height: 1;
    color: var(--leaf);
  }
  .brand-tagline {
    font-family: "Quicksand", sans-serif;
    font-weight: 500;
    font-size: 30px;
    line-height: 1.2;
    color: #9cbf36;
    margin-left: 150px;
  }
  .phone-pill {
    position: absolute;
    left: 330px;
    top: 380px;
    height: 62px;
    padding: 0 30px 0 6px;
    display: flex;
    align-items: center;
    gap: 16px;
    border-radius: 31px;
    background: var(--forest);
    font-family: "Open Sans", sans-serif;
    font-weight: 700;
    font-size: 30px;
    color: var(--white);
    letter-spacing: 1px;
  }
  .phone-icon {
    width: 50px;
    height: 50px;
    border-radius: 50%;
    background: var(--ring);
    display: flex;
    align-items: center;
    justify-content: center;
  }
  .skyline-disc {
    position: absolute;
    left: 470px;
    top: -150px;
    width: 340px;
    height: 340px;
    border-radius: 50%;
    border: 34px solid var(--ring);
    box-sizing: border-box;
    background: linear-gradient(180deg, var(--cream) 0%, #cfe7a6 55%, var(--ring-deep) 100%);
  }
  .laundry-photo {
    position: absolute;
    left: 790px;
    top: 0;
    width: 190px;
    height: 470px;
    background: linear-gradient(160deg, var(--pink) 0%, var(--fuchsia) 35%, #c42a3a 60%, #f4eef0 100%);
  }
  .address-band {
    position: absolute;
    left: 330px;
    right: 0;
    bottom: 0;
    height: 90px;
    background: var(--forest);
    display: flex;
    align-items: center;
    padding-left: 28px;
    font-family: "Open Sans", sans-serif;
    font-weight: 700;
    font-size: 30px;
    color: var(--white);
    letter-spacing: 1px;
    text-transform: uppercase;
    white-space: nowrap;
  }
</style>
</head>
<body>
  <div class="business-card">
    <div class="skyline-disc" role="img" aria-label="Green city skyline silhouette inside a circular frame"></div>
    <div class="laundry-photo" role="img" aria-label="Photo of folded colourful laundry in pink, red and white"></div>

    <div class="brand">
      <span class="brand-dot"></span>
      <div class="brand-text">
        <span class="brand-name">Tumble Nook</span>
        <span class="brand-tagline">Laundromat</span>
      </div>
    </div>

    <div class="phone-pill">
      <span class="phone-icon">
        <svg width="28" height="28" viewBox="0 0 24 24" aria-hidden="true">
          <path fill="#1e8c3a" d="M6.6 10.8a15.1 15.1 0 0 0 6.6 6.6l2.2-2.2a1 1 0 0 1 1-.25 11.4 11.4 0 0 0 3.6.57 1 1 0 0 1 1 1V20a1 1 0 0 1-1 1A17 17 0 0 1 3 4a1 1 0 0 1 1-1h3.5a1 1 0 0 1 1 1c0 1.25.2 2.45.57 3.6a1 1 0 0 1-.25 1z"/>
        </svg>
      </span>
      <span class="phone-number">0961 472 850</span>
    </div>

    <div class="address-band">284 Colbrook Street Lynn MA 01957</div>
  </div>
</body>
</html>
```